Microlight Aircraft Website Project

Need a website designed, or at least a template made, that my web programmer can work with here. We are a new manufacturer of microlight aircraft & powered hang gliders. Our company name is Brisk Fern. We manufacture portable utility aircraft in the Light Sport category (formerly known as Ultralights or Microlights). Our particular design is a 2-seat powered hang glider and caters to those who want to go explore the backcountry. We are not necessarily aviation nuts, but more into the development of a flying utility vehicle for extreme exploration and expeditions. We have been importing these aircraft from 3 countries for 15 years and have supplied over 200 expedition-quality aircraft world-wide. We are now manufacturing here in the US.

Industry/Entity Type

Manufacturer

Coding

Coded - Design and coding required

```html
<!DOCTYPE html>
<html lang="en">
<head>
<meta charset="utf-8">
<title>Brisk Fern — Microlight Aircraft &amp; Powered Hang Gliders</title>
<link rel="stylesheet" href="https://fonts.googleapis.com/css2?family=Michroma&family=Open+Sans:ital,wght@0,400;0,600;0,700;1,400&family=Poppins:wght@400;500&display=swap">
<style>
:root{
  --blue:#0457a8;
  --sky:#1ba8e0;
  --ink:#333;
  --heading:#1c1c1c;
  --grey-band:#e6e6e6;
  --footer:#222222;
  --footer-base:#1a1a1a;
  --footer-text:#9a9a9a;
  --signup:#1736c4;
  --white:#fff;
}
*{box-sizing:border-box;margin:0;padding:0}
html,body{width:1200px;height:2329px;overflow:hidden}
body{position:relative;background:var(--white);font-family:"Open Sans",sans-serif;color:var(--ink)}
.abs{position:absolute}

/* header */
.site-header{position:absolute;left:0;top:0;width:1200px;height:157px;background:var(--white)}
.brand{position:absolute;left:58px;top:46px;display:flex;align-items:center;gap:14px}
.brand-dot{width:34px;height:34px;border-radius:50%;background:var(--blue)}
.brand-name{font-family:"Open Sans",sans-serif;font-weight:700;font-size:34px;color:var(--blue);letter-spacing:.5px}
.contact-pill{position:absolute;top:54px;height:64px;border-radius:32px;background:linear-gradient(90deg,#ececec,#f8f8f8 70%,#fff);display:flex;align-items:center;padding-left:22px;gap:14px}
.contact-pill.call{left:606px;width:240px}
.contact-pill.mail{left:850px;width:260px}
.contact-pill .label{font-family:"Poppins",sans-serif;font-size:15px;color:#333;line-height:1;margin-left:30px;margin-bottom:4px}
.contact-pill .value{font-family:"Open Sans",sans-serif;font-weight:700;font-size:21px;color:#111;line-height:1.1}
.contact-pill.mail .value{font-size:19px}

/* nav */
.main-nav{position:absolute;left:0;top:157px;width:1200px;height:56px;background:var(--blue)}
.main-nav a{position:absolute;top:0;height:56px;line-height:56px;color:var(--white);text-decoration:none;font-weight:600;font-size:16px}
.main-nav a.active{background:var(--sky);top:4px;height:48px;line-height:48px;padding:0 15px}

/* hero */
.hero{position:absolute;left:0;top:213px;width:1200px;height:473px;background:linear-gradient(180deg,#d8cfc7 0%,#c89a70 30%,#b5502a 60%,#7c2a14 100%)}
.hero-title{position:absolute;left:68px;top:170px;font-family:"Michroma",sans-serif;font-size:35px;color:var(--white);letter-spacing:1px}
.hero-sub{position:absolute;left:68px;top:225px;font-size:16px;color:var(--white);text-transform:uppercase}
.hero-btn{position:absolute;left:73px;top:267px;width:144px;height:49px;border:2px solid var(--white);color:var(--white);font-weight:700;font-size:15px;text-align:center;line-height:45px}

/* welcome */
.section-title{position:absolute;left:0;width:1200px;text-align:center;font-family:"Michroma",sans-serif;font-weight:400;color:var(--heading)}
.welcome-title{top:746px;font-size:33px}
.divider{position:absolute;left:525px;top:811px;width:150px;height:4px}
.welcome-copy{position:absolute;left:100px;top:846px;width:1000px;text-align:center;font-size:15.5px;line-height:24px;color:#444}
.welcome-copy p+p{margin-top:24px}

/* aircraft types */
.aircraft-band{position:absolute;left:0;top:1046px;width:1200px;height:386px;background:var(--grey-band)}
.aircraft-card{position:absolute;top:1115px;width:325px;height:243px}
.aircraft-photo{width:325px;height:191px}
.aircraft-label{height:52px;background:var(--blue);display:flex;align-items:center;justify-content:space-between;padding:0 16px 0 22px;color:var(--white);font-family:"Michroma",sans-serif;font-size:17px}
.arrow-btn{width:38px;height:38px}

/* testimonials */
.testi-title{top:1503px;font-size:37px}
.testi-quote{position:absolute;left:100px;top:1596px;width:1000px;text-align:center;font-family:Arial,sans-serif;font-style:italic;font-size:16.5px;line-height:25px;color:#333}
.avatar{position:absolute;left:545px;top:1670px;width:114px;height:114px;border-radius:50%;border:4px solid #f0f0f0;background:linear-gradient(180deg,#9fb3c2,#dfe5ea);box-shadow:0 0 0 1px #d8d8d8}
.quote-badge{position:absolute;left:539px;top:1672px;width:36px;height:36px;border-radius:50%;background:#222;color:#fff;font-family:Georgia,serif;font-size:26px;font-weight:700;text-align:center;line-height:44px}
.testi-name{position:absolute;left:0;top:1821px;width:1200px;text-align:center;font-family:Arial,sans-serif;font-size:16px;color:#222}
.testi-name strong{font-style:italic}
.testi-name em{color:#444}
.dots{position:absolute;left:550px;top:1881px;display:flex;gap:6px}
.dots span{width:31px;height:5px;background:#c9c9c9}
.dots span.on{background:var(--blue)}

/* footer */
.site-footer{position:absolute;left:0;top:1957px;width:1200px;height:325px;background:var(--footer)}
.footer-base{position:absolute;left:0;top:2282px;width:1200px;height:47px;background:var(--footer-base);text-align:center;line-height:47px;font-size:12.5px;color:#7d7d7d;letter-spacing:.3px}
.footer-brand{position:absolute;left:70px;top:2037px;display:flex;align-items:center;gap:10px}
.footer-brand .brand-dot{width:26px;height:26px;background:#8a8a8a}
.footer-brand .brand-name{color:#b4b4b4;font-size:27px}
.footer-about{position:absolute;left:60px;top:2095px;width:230px;font-size:12.5px;line-height:22px;color:var(--footer-text)}
.social{position:absolute;top:2194px;width:30px;height:30px;border-radius:50%;background:#5a5a5a}
.footer-head{position:absolute;top:1993px;font-weight:700;font-size:14px;color:var(--white);letter-spacing:.3px}
.touch-item{position:absolute;left:335px;display:flex;gap:12px;font-family:"Poppins",sans-serif;font-size:11.5px;line-height:20px;color:#bdbdbd}
.touch-item svg{flex:none;margin-top:4px}
.info-item{position:absolute;left:613px;font-size:12.5px;color:#9a9a9a;text-transform:uppercase}
.info-item::before{content:"›";color:#3b6fd1;margin-right:12px}
.news-copy{position:absolute;left:890px;top:2040px;width:250px;font-family:"Poppins",sans-serif;font-size:12.5px;line-height:28px;color:var(--footer-text)}
.news-input{position:absolute;left:890px;top:2132px;width:250px;height:46px;border:1px solid #4a4a4a;color:#cfcfcf;font-family:"Poppins",sans-serif;font-size:13px;line-height:44px;padding-left:18px}
.news-btn{position:absolute;left:890px;top:2198px;width:250px;height:43px;background:var(--signup);color:var(--white);font-family:"Poppins",sans-serif;font-weight:500;font-size:13px;text-align:center;line-height:43px}
</style>
</head>
<body>

<header class="site-header">
  <div class="brand"><span class="brand-dot"></span><span class="brand-name">Brisk Fern</span></div>

  <div class="contact-pill call">
    <svg width="24" height="22" viewBox="0 0 24 22" aria-hidden="true"><path d="M3 8c0-4 18-4 18 0v2h-5V8H8v2H3z M6 11h12l2 9H4z" fill="#777"/></svg>
    <div><div class="label">(Call us)</div><div class="value">+1800-555-20917</div></div>
  </div>
  <div class="contact-pill mail">
    <svg width="22" height="22" viewBox="0 0 22 22" aria-hidden="true"><rect x="2" y="3" width="18" height="16" rx="2" fill="none" stroke="#777" stroke-width="2"/><path d="M6 8h10M6 12h10M6 16h6" stroke="#777" stroke-width="1.6"/></svg>
    <div><div class="label">(E-mail)</div><div class="value">hello@briskfern.com</div></div>
  </div>
</header>

<nav class="main-nav">
  <a class="active" href="#" style="left:74px">HOME</a>
  <a href="#" style="left:196px">ABOUT US</a>
  <a href="#" style="left:335px">AIRCRAFT TYPE</a>
  <a href="#" style="left:512px">OUR SERVICES</a>
  <a href="#" style="left:682px">BLOG</a>
  <a href="#" style="left:784px">CONTACT US</a>
</nav>

<section class="hero" role="img" aria-label="Photo of a two-seat powered hang glider flying over red sandstone canyons at sunset">
  <h1 class="hero-title">NEW MANUFACTURER</h1>
  <p class="hero-sub">Of microlight aircraft &amp; powered hang gliders</p>
  <div class="hero-btn">READ MORE</div>
</section>

<h2 class="section-title welcome-title">WELCOME TO BRISK FERN</h2>
<svg class="divider" viewBox="0 0 150 4" aria-hidden="true"><rect x="0" y="1" width="68" height="2" fill="#0457a8"/><rect x="82" y="1" width="68" height="2" fill="#0457a8"/><path d="M70 4l4-4M75 4l4-4" stroke="#0457a8" stroke-width="1.5"/></svg>
<div class="welcome-copy">
  <p>We will assign a project manager, field superintendent, engineer and other staff members as required to effectively manage the construction process. Praesent dapibus, neque id cursus faucibus, tortor neque egestas augue, eu vulputate magna eros eu erat. Aliquam erat volutpat. Nam dui mi, tincidunt quis, accumsan porttitor, facilisis luctus, metus.</p>
  <p>During the construction of any project, the coordination of the trades is an integral part of the process, especially with respect to the mechanical and electrical trades.</p>
</div>

<section class="aircraft-band"></section>
<article class="aircraft-card" style="left:73px">
  <div class="aircraft-photo" role="img" aria-label="Photo of a yellow microlight trike with a striped wing against a deep blue sky" style="background:linear-gradient(160deg,#1c2f8c,#3d5cc0 60%,#c9d3e6)"></div>
  <div class="aircraft-label"><span>MICROLIGHT AIRCRAFT</span><svg class="arrow-btn" viewBox="0 0 38 38" aria-hidden="true"><circle cx="19" cy="19" r="19" fill="#1ba8e0"/><path d="M10 19h17M20 12l7 7-7 7" stroke="#fff" stroke-width="3" fill="none" stroke-linecap="round"/></svg></div>
</article>
<article class="aircraft-card" style="left:435px">
  <div class="aircraft-photo" role="img" aria-label="Photo of a red microlight trike in flight above a coastline" style="background:linear-gradient(180deg,#b8242a 0%,#d9d0c6 35%,#6f8fa0 65%,#7a6a4c 100%)"></div>
  <div class="aircraft-label"><span>MICROLIGHT AIRCRAFT</span><svg class="arrow-btn" viewBox="0 0 38 38" aria-hidden="true"><circle cx="19" cy="19" r="19" fill="#1ba8e0"/><path d="M10 19h17M20 12l7 7-7 7" stroke="#fff" stroke-width="3" fill="none" stroke-linecap="round"/></svg></div>
</article>
<article class="aircraft-card" style="left:800px">
  <div class="aircraft-photo" role="img" aria-label="Photo of a microlight trike with a red and yellow wing parked on an airfield" style="background:linear-gradient(180deg,#9fb2c6 0%,#d6dde3 45%,#6f7a58 62%,#4b4e52 100%)"></div>
  <div class="aircraft-label"><span>MICROLIGHT AIRCRAFT</span><svg class="arrow-btn" viewBox="0 0 38 38" aria-hidden="true"><circle cx="19" cy="19" r="19" fill="#1ba8e0"/><path d="M10 19h17M20 12l7 7-7 7" stroke="#fff" stroke-width="3" fill="none" stroke-linecap="round"/></svg></div>
</article>

<h2 class="section-title testi-title">WHAT PEOPLE SAY</h2>
<p class="testi-quote">"Lorem ipsum dolor sit amet, consectetur adipiscing elit. Morbi hendrerit elit turpis, a porttitor tellus sollicitudin at. Class aptent taciti sociosqu ad litora torquent per conubia nostra, per inceptos himenaeos."</p>
<div class="avatar" role="img" aria-label="Portrait photo of the customer"></div>
<div class="quote-badge" aria-hidden="true">“</div>
<p class="testi-name"><strong>MARLA QUENTIN</strong> <em>Fitness Enthusiast, DUNMORE</em></p>
<div class="dots"><span class="on"></span><span></span><span></span><span></span></div>

<footer class="site-footer"></footer>
<div class="footer-brand"><span class="brand-dot"></span><span class="brand-name">Brisk Fern</span></div>
<p class="footer-about">Kestrel Lane and member of the Harlow Valley Trade Builders Association.</p>
<span class="social" style="left:60px"></span>
<span class="social" style="left:100px"></span>
<span class="social" style="left:141px"></span>
<span class="social" style="left:181px"></span>

<h3 class="footer-head" style="left:335px">GET IN TOUCH</h3>
<div class="touch-item" style="top:2040px"><svg width="10" height="13" viewBox="0 0 10 13"><path d="M5 0a5 5 0 0 1 5 5c0 3-5 8-5 8S0 8 0 5a5 5 0 0 1 5-5z" fill="#3b6fd1"/><circle cx="5" cy="5" r="1.8" fill="#222"/></svg><span>2817 Alder Ave. Pine Hollow, OR 97402.<br>United States</span></div>
<div class="touch-item" style="top:2096px"><svg width="12" height="12" viewBox="0 0 12 12"><path d="M2 0l3 3-1.5 2a7 7 0 0 0 3.5 3.5L9 7l3 3-2 2C5 12 0 7 0 2z" fill="#3b6fd1"/></svg><span>(555) 20917364</span></div>
<div class="touch-item" style="top:2131px"><svg width="12" height="12" viewBox="0 0 12 12"><path d="M0 5L12 0 8 12 6 7z" fill="#3b6fd1"/></svg><span>mail@fernhangar.com</span></div>
<div class="touch-item" style="top:2166px"><svg width="9" height="13" viewBox="0 0 9 13"><rect x="0.75" y="0.75" width="7.5" height="11.5" rx="1.5" fill="none" stroke="#3b6fd1" stroke-width="1.5"/></svg><span>(555) 20917364</span></div>
<div class="touch-item" style="top:2200px"><svg width="12" height="12" viewBox="0 0 12 12"><circle cx="6" cy="6" r="5.2" fill="none" stroke="#3b6fd1" stroke-width="1.5"/><path d="M6 3v3.3l2 1.3" stroke="#3b6fd1" stroke-width="1.4" fill="none"/></svg><span>Mon - Sat: 9:00 - 18:00</span></div>

<h3 class="footer-head" style="left:613px">INFORMATION</h3>
<div class="info-item" style="top:2043px">Wine</div>
<div class="info-item" style="top:2078px">Events</div>
<div class="info-item" style="top:2113px">Gallery</div>
<div class="info-item" style="top:2148px">About us</div>
<div class="info-item" style="top:2183px">Members</div>
<div class="info-item" style="top:2218px">Outlets</div>

<h3 class="footer-head" style="left:890px">NEWS LETTER</h3>
<p class="news-copy">Enter your email address for our mailing list to keep your self our lastest updated.</p>
<div class="news-input">Email</div>
<div class="news-btn">Sign up</div>

<div class="footer-base">COPYRIGHT © 2007 - 2016 BRISK FERN.&nbsp; ALL RIGHTS RESERVED</div>

</body>
</html>
```